Innovative mission-driven diversity services company needs launch brochure

Two-sided 8 1/5" x 11" document to demonstrate a new program.

Target Market(s)

Chief Diversity Officers and Hiring Managers at advertising/communications agencies who are looking to attract and hire recently graduated/about to graduate African American students

Industry/Entity Type

It Company

Requirements
Must have
• a very contemporary feel that will well represent the vibrancy, energy, and identity of the African American student population. This is a cause driven organization and that passion and purpose should be conveyed while recognizing that the target audience are corporate executives.

```html
<!DOCTYPE html>
<html lang="en">
<head>
<meta charset="utf-8">
<title>Parity Point LLC – Launch Brochure</title>
<link rel="stylesheet" href="https://fonts.googleapis.com/css2?family=Source+Sans+3:ital,wght@0,400;0,600;0,700;1,400&display=swap">
<style>
:root{
  --bg:#d9d4cd;
  --paper:#ffffff;
  --brown:#7d5b3c;
  --brown-dark:#4b2f1b;
  --ink-dark:#2c1b10;
  --accent:#8a4a1d;
  --text:#2a2a2a;
  --footer:#111111;
  --banner:rgba(66,40,22,.88);
}
*{margin:0;padding:0;box-sizing:border-box}
html,body{width:1200px;height:852px;overflow:hidden;background:var(--bg);font-family:"Source Sans 3",sans-serif;color:var(--text)}
.canvas{position:relative;width:1200px;height:852px}
.page{position:absolute;width:498px;height:645px;background:var(--paper);overflow:hidden;box-shadow:0 2px 8px rgba(0,0,0,.15)}
.page--front{left:50px;top:52px}
.page--back{left:627px;top:139px}
.abs{position:absolute}

/* Front */
.brand-name{left:22px;top:20px;font-size:32px;font-weight:600;color:var(--ink-dark);line-height:1;letter-spacing:-.3px;white-space:nowrap}
.brand-sub{left:24px;top:60px;font-size:10px;color:var(--ink-dark)}
.tagline{left:300px;top:28px;width:180px;font-size:10px;line-height:13px;text-align:center;color:var(--ink-dark)}
.rule{left:0;top:87px;width:498px;height:5px;background:var(--brown)}
.hero{left:0;top:92px;width:498px;height:244px;background:linear-gradient(160deg,#a88870 0%,#5a4334 45%,#2a1d16 100%)}
.hero-banner{left:0;top:276px;width:498px;height:60px;background:var(--banner);color:#fff;font-size:11.8px;font-weight:600;line-height:17px;text-align:center;padding-top:13px;white-space:nowrap}
.sidebar{left:0;top:336px;width:162px;height:274px;background:var(--brown);color:#fff}
.sidebar-q{left:8px;top:10px;width:146px;font-size:8.3px;font-style:italic;line-height:11px;text-align:center}
.thumb{left:45px;width:64px;height:42px;border:1.5px solid #fff}
.thumb--one{top:42px;background:linear-gradient(135deg,#b45a3c,#3a2a2a)}
.thumb--two{top:112px;background:linear-gradient(90deg,#d9a85a,#e9dccb 45%,#b84a3a)}
.thumb--three{top:192px;background:linear-gradient(135deg,#e9e4dc,#3a3030)}
.caption{left:8px;width:146px;font-size:6.8px;font-style:italic;line-height:8.8px;text-align:center}
.caption--one{top:87px}
.caption--two{top:160px}
.caption--three{top:238px}
.chart-title{left:177px;top:347px;font-size:9.6px;font-style:italic;color:#444}
.chart{left:0;top:0}
.chart text{font-family:"Source Sans 3",sans-serif;fill:#333}
.body-copy{left:176px;top:457px;width:306px;font-size:7.2px;line-height:9.2px;color:#333}
.ref{left:176px;top:501px;font-size:7.2px;color:#333}
.clients{left:177px;top:521px;font-size:9.6px;font-style:italic;color:#444}
.news-card{left:175px;top:541px;width:113px;height:59px;border:1px solid #555;padding:4px 6px}
.news-kicker{font-size:3.5px;color:#777;letter-spacing:.3px}
.news-head{font-size:7.7px;font-weight:700;line-height:8.5px;color:#111;margin-top:1px}
.share{display:flex;gap:2px;margin-top:3px}
.share span{display:block;width:9px;height:3px}
.news-byline{font-size:3.6px;color:#777;margin-top:3px}
.quote-card{left:297px;top:541px;width:189px;height:59px;border:1px solid #555}
.quote-photo{left:0;top:0;width:55px;height:57px;background:linear-gradient(160deg,#8a7c70,#3b3531)}
.quote-text{left:61px;top:5px;width:124px;font-size:6.8px;font-style:italic;line-height:9px;color:#333}
.front-footer{left:0;top:610px;width:498px;height:35px;background:var(--footer);color:#fff;font-size:6.8px;padding:13px 0 0 20px;white-space:nowrap}

/* Back */
.about-col{left:314px;top:0;width:184px;height:645px;background:var(--brown)}
.portrait{left:289px;top:20px;width:114px;height:123px;background:#fff;padding:4px}
.portrait-fill{width:100%;height:100%;background:linear-gradient(150deg,#9a8a74 0%,#5c4536 55%,#2c2620 100%)}
.mission-title{left:22px;top:50px;font-size:24px;font-weight:600;color:var(--accent);letter-spacing:-.3px;white-space:nowrap}
.mission-text{left:22px;top:92px;width:250px;font-size:10.4px;font-weight:600;line-height:14.6px;color:var(--accent);text-align:justify}
.process-title{left:23px;top:162px;font-size:24px;font-weight:600;color:var(--accent)}
.process{left:23px;top:198px;width:275px}
.step h3{font-size:13.2px;font-weight:600;color:var(--accent);line-height:17px}
.step p{font-size:10.2px;line-height:14.6px;color:#222}
.step{margin-bottom:8px}
.step p+p{margin-top:4px}
.about-title{left:335px;top:208px;font-size:16px;font-weight:600;color:#fff;white-space:nowrap;line-height:20px}
.about-body{left:335px;top:238px;width:150px;font-size:8.6px;line-height:11.3px;color:#fff}
.about-body p+p{margin-top:11px}
</style>
</head>
<body>
<main class="canvas">

  <section class="page page--front" aria-label="Brochure front">
    <div class="abs brand-name">Parity Point LLC</div>
    <div class="abs brand-sub">Narrowing The Racial Diversity Gap</div>
    <p class="abs tagline">A powerful new approach to increasing the African-American employment rate in the communications industry</p>
    <div class="abs rule"></div>
    <div class="abs hero" role="img" aria-label="Photo of smiling graduates in caps and gowns"></div>
    <h2 class="abs hero-banner">Despite efforts to increase participation, African-American rates of employment<br>in the communications industry have actually declined over the past decade</h2>

    <aside class="abs sidebar">
      <p class="abs sidebar-q">Why are communications agencies failing to increase the AA hiring rate?</p>
      <div class="abs thumb thumb--one" role="img" aria-label="Photo of an industry panel discussion"></div>
      <p class="abs caption caption--one">An industry too inwardly focused<br>to realize that it can be offputting</p>
      <div class="abs thumb thumb--two" role="img" aria-label="Illustration of a face split into colourful patterned halves"></div>
      <p class="abs caption caption--two">Assuming barriers to hiring all people of color are the same and are not unique to each group</p>
      <div class="abs thumb thumb--three" role="img" aria-label="Photo of a young man holding a hand-written sign"></div>
      <p class="abs caption caption--three">Dramatic disconnection from the most critical candidate pool that can provide an immediate and lasting impact</p>
    </aside>

    <p class="abs chart-title">African-American Proportion of Workforce*</p>
    <svg class="abs chart" width="498" height="645" viewBox="0 0 498 645" aria-label="Bar chart comparing overall workforce and communications industry shares in 2005 and 2016">
      <defs>
        <linearGradient id="bar" x1="0" y1="0" x2="0" y2="1">
          <stop offset="0" stop-color="#6a3f1f"/><stop offset="1" stop-color="#3e2412"/>
        </linearGradient>
      </defs>
      <rect x="204" y="375" width="42" height="52" fill="url(#bar)"/>
      <rect x="264" y="395" width="43" height="32" fill="url(#bar)"/>
      <rect x="360" y="375" width="42" height="52" fill="url(#bar)"/>
      <rect x="427" y="405" width="42" height="22" fill="url(#bar)"/>
      <line x1="176" y1="428" x2="481" y2="428" stroke="#666" stroke-width="1"/>
      <text x="285" y="388" font-size="8" text-anchor="middle">2005</text>
      <text x="448" y="388" font-size="8" text-anchor="middle">2016</text>
      <g font-size="6.4" text-anchor="middle">
        <text x="225" y="439">Overall</text><text x="225" y="448">Workforce</text>
        <text x="286" y="439">Communications</text><text x="286" y="448">Industry</text>
        <text x="381" y="439">Overall</text><text x="381" y="448">Workforce</text>
        <text x="448" y="439">Communications</text><text x="448" y="448">Industry</text>
      </g>
    </svg>
    <p class="abs body-copy">While the communications agency hiring rate of people of Hispanic or Asian origin has reached parity with their overall workforce participation rates, African-American participation has actually dropped by nearly a third. Communications agencies have identified this gap as a critical issue but are falling further behind on AA hiring.</p>
    <p class="abs ref">*REFERENCE TO COME</p>
    <p class="abs clients">Clients have now begun to directly exert pressure on the industry</p>

    <article class="abs news-card">
      <div class="news-kicker">BRANDS</div>
      <div class="news-head">Harvest Table Foods Insists That Its Future Agencies Meet Specific Diversity Quotas</div>
      <div class="share"><span style="background:#4a5f8a"></span><span style="background:#5aa2d6"></span><span style="background:#c44"></span></div>
      <div class="news-byline">By Staff Writer · Aug 2016</div>
    </article>
    <article class="abs quote-card">
      <div class="abs quote-photo" role="img" aria-label="Portrait photo of a speaking executive"></div>
      <p class="abs quote-text">“In order to push yourself to have a more diverse work force you have to be intentional about it — and nothing will drive intent faster than a client’s dollar”</p>
    </article>

    <footer class="abs front-footer">Parity Point is a B Corp (for-profit social enterprise) created by two principles with direct and complimentary experiences in tackling related challenges.</footer>
  </section>

  <section class="page page--back" aria-label="Brochure back">
    <div class="abs about-col"></div>
    <div class="abs portrait"><div class="portrait-fill" role="img" aria-label="Photo of a smiling student with a backpack on campus"></div></div>

    <h2 class="abs mission-title">THE PARITY MISSION</h2>
    <p class="abs mission-text">Drive parity in opportunity and representation for the most promising young African-American minds while creating a cultural and competitive advantage for progressive communications organizations</p>

    <h2 class="abs process-title">PROCESS</h2>
    <div class="abs process">
      <div class="step"><h3>1. Community Connection</h3><p>Parity Point works closely with the African-American communities within relevant college programs with a strong focus on HBCUs</p></div>
      <div class="step"><h3>2. Identification &amp; Vetting</h3><p>Candidates are identified through community connection and formally assessed for relevant agency technology skills, emotional, cultural and academic prowess.</p></div>
      <div class="step"><h3>3. Multi-Focal Training</h3><p>Training program specific to advertising industry, to include all major disciplines.</p><p>Coaching provided to crystallize candidate’s personal brand and voice, to improve the communication of value and reduce time spent ‘trying to figure out.’ Coaching also focuses on personal presentation and professional etiquette training to facilitate corporate integration.</p></div>
      <div class="step"><h3>4. Onboarding Support</h3><p>New hires will be provided innovative e-development platform with personal mentor, to ensure successful onboarding.</p></div>
      <div class="step"><h3>5. Community Building</h3><p>Each Parity Point candidate signs an agreement to initiate a mentoring relationship with a young African American professional hired after them within their organization.</p></div>
    </div>

    <h2 class="abs about-title">ABOUT PARITY POINT</h2>
    <div class="abs about-body">
      <p>Parity Point is a B Corp (for-profit social enterprise) created by two principles with direct and complimentary experiences in tackling related challenges.</p>
      <p>Renee Calloway has created a highly successful coaching practice focused on helping soon to graduate, or recently graduated, college students find purpose-driven careers. She is also the founder and Executive Director of the RCW Foundation which provides guidance and assistance for young adults who are “aging out” of the welfare system with over half of the foundation’s fellows being African-American.</p>
      <p>Martin Ashford spent his career in the advertising business culminating in running leading agencies at both Meridian Group and Crestline Partners. He has personally dealt with the barriers and frustrations in identifying and attracting talent from the African-American business community despite significant corporate efforts. He has also witnessed the significant advantages gained when truly diversified teams are assembled and nurtured.</p>
    </div>
  </section>

</main>
</body>
</html>
```